Personalized Technology Company Needs a Business Card

I need a double-sided business card. Both sides will have the logo, and the contact information. One side will be black, with the white / gray logo, and the other will be white, with the black / gray logo. The black side will have the text "Custom Gaming PC's" and will have a water-cooled gaming PC image. The white side will have the text "Custom Business Computers & Consulting", and will have a business / enterprise PC image. Feel free to add a conservative image in the background, while the color remains unchanged. I'm uploading the base logo (transparent), so you can modify the colors, both the finished colored logos and an idea of ​​the business card (with the current information, just missing the website, which is www.velmorisystems.com, please add it.) Thank you so much for your effort, I'll be specting your cool designs. Good Luck!

Target Market(s)

Gamers & Entrepreneurs / Business Owners / Chief Technology Officers

Industry/Entity Type

Technology Equipment

Contact Information for Business Card

I need a double-sided business card. Both sides will have the logo, and the contact information. One side will be black, with the white/gray logo, and the other one will be white, with the black/gray logo. The black side will have the text "Custom Gaming PC's" and will have a water-cooled gaming PC image. The white side will have the text "Custom Business Computers & Consulting", and will have a business/enterprise PC image. Feel free to add a conservative image in the background, whilst the color remains unchanged.

I'm uploading the base logo (transparent), so you can modify the colors, both the finished colored logos and an idea of the business card (with the actual information, just missing the website, which is www.velmorisystems.com, please add it.)

Thank you so much for your effort, I'll be specting your cool designs. Good Luck!

Font styles to use
Serif

Colors
000000
757575
ffffff

Requirements
Must have
• Please See Description
Nice to have
• Please See Description
Should not have
• Please See Description

```html
<!DOCTYPE html>
<html lang="en">
<head>
<meta charset="utf-8">
<title>Velmori Systems – Business Cards</title>
<link href="https://fonts.googleapis.com/css2?family=Roboto+Slab:wght@400;500;700&display=swap" rel="stylesheet">
<style>
  :root {
    --black: #000000;
    --ink: #141414;
    --gray: #757575;
    --light-gray: #e4e4e4;
    --paper: #f3f3f1;
    --white: #ffffff;
    --sand: #cbbfb2;
    --backdrop: #dcdcdc;
  }
  * { margin: 0; padding: 0; box-sizing: border-box; }
  html, body { width: 1198px; height: 1200px; overflow: hidden; }
  body {
    background: var(--backdrop);
    font-family: "Roboto Slab", Georgia, serif;
    position: relative;
  }
  .card {
    position: absolute;
    left: 99px;
    width: 1000px;
    height: 540px;
    overflow: hidden;
    box-shadow: 0 8px 24px rgba(0,0,0,.18);
  }
  .card--business { top: 40px; background: var(--paper); color: var(--ink); }
  .card--gaming { top: 620px; background: var(--black); color: var(--white); }

  .photo { position: absolute; top: 0; left: 0; height: 100%; }
  .card--business .photo {
    width: 440px;
    background: linear-gradient(135deg, #d9d4cc 0%, #bdb8b0 40%, #6e6a66 70%, #cfc9c0 100%);
    border-right: 10px solid var(--black);
  }
  .card--gaming .photo {
    width: 400px;
    background: radial-gradient(ellipse at 55% 35%, #3f8f8a 0%, #1c3f44 28%, #0b1418 60%, #000 100%);
  }

  .divider { position: absolute; left: 425px; width: 3px; background: var(--sand); }
  .divider--top { top: 0; height: 110px; }
  .divider--bottom { bottom: 0; height: 70px; }

  .brand {
    position: absolute;
    top: 55px;
    right: 60px;
    display: flex;
    align-items: center;
    gap: 12px;
    font-weight: 500;
    font-size: 30px;
    letter-spacing: 4px;
  }
  .brand__mark { width: 22px; height: 22px; }
  .card--business .brand { color: var(--black); }
  .card--business .brand__mark { background: var(--gray); }
  .card--gaming .brand { color: var(--white); }
  .card--gaming .brand__mark { background: var(--sand); }

  .person { position: absolute; top: 135px; }
  .card--business .person { left: 490px; }
  .card--gaming .person { left: 460px; }
  .person__name { font-weight: 700; font-size: 32px; line-height: 1; }
  .person__title { font-size: 22px; margin-top: 8px; }
  .card--gaming .person__title { color: var(--sand); }

  .contacts { position: absolute; top: 230px; list-style: none; }
  .card--business .contacts { left: 440px; }
  .card--gaming .contacts { left: 450px; }
  .contact { display: flex; align-items: center; height: 46px; margin-bottom: 8px; }
  .contact__tag { width: 92px; height: 46px; flex: none; }
  .contact__text { margin-left: 22px; font-size: 22px; line-height: 1; }
  .card--business .contact__text { font-weight: 500; }

  .tagline {
    position: absolute;
    right: 50px;
    bottom: 38px;
    font-size: 20px;
  }
  .card--gaming .tagline { color: #b8b8b8; }
</style>
</head>
<body>

<svg width="0" height="0" style="position:absolute">
  <defs>
    <symbol id="icon-phone" viewBox="0 0 24 24"><path d="M6.6 10.8a15 15 0 0 0 6.6 6.6l2.2-2.2a1 1 0 0 1 1-.25 11 11 0 0 0 3.6.6 1 1 0 0 1 1 1V20a1 1 0 0 1-1 1A17 17 0 0 1 3 4a1 1 0 0 1 1-1h3.5a1 1 0 0 1 1 1 11 11 0 0 0 .6 3.6 1 1 0 0 1-.25 1z"/></symbol>
    <symbol id="icon-mobile" viewBox="0 0 24 24"><rect x="6" y="2" width="12" height="20" rx="2" fill="none" stroke-width="2"/></symbol>
    <symbol id="icon-mail" viewBox="0 0 24 24"><rect x="2" y="5" width="20" height="14" fill="none" stroke-width="2"/><path d="M2 5l10 8 10-8" fill="none" stroke-width="2"/></symbol>
    <symbol id="icon-web" viewBox="0 0 24 24"><circle cx="12" cy="12" r="9" fill="none" stroke-width="2"/><ellipse cx="12" cy="12" rx="4" ry="9" fill="none" stroke-width="2"/><path d="M3 12h18" fill="none" stroke-width="2"/></symbol>
  </defs>
</svg>

<!-- White side -->
<section class="card card--business">
  <div class="photo" role="img" aria-label="Photo of hands working on a laptop showing business charts"></div>
  <div class="brand"><span class="brand__mark"></span>VELMORI</div>
  <div class="person">
    <p class="person__name">MARCO RUIZ DELAN</p>
    <p class="person__title">CEO &amp; Co-Founder</p>
  </div>
  <ul class="contacts">
    <li class="contact">
      <svg class="contact__tag" viewBox="0 0 92 46"><path d="M0 0H68L92 23L68 46H0Z" fill="#000"/><use href="#icon-phone" x="22" y="11" width="24" height="24" fill="#e4e4e4" stroke="#e4e4e4"/></svg>
      <span class="contact__text">+52 5812 - 3390</span>
    </li>
    <li class="contact">
      <svg class="contact__tag" viewBox="0 0 92 46"><path d="M0 0H68L92 23L68 46H0Z" fill="#000"/><use href="#icon-mobile" x="22" y="11" width="24" height="24" stroke="#e4e4e4"/></svg>
      <span class="contact__text">+52 55 - 4168 - 0937</span>
    </li>
    <li class="contact">
      <svg class="contact__tag" viewBox="0 0 92 46"><path d="M0 0H68L92 23L68 46H0Z" fill="#000"/><use href="#icon-mail" x="22" y="11" width="24" height="24" stroke="#e4e4e4"/></svg>
      <span class="contact__text">contact@velmorisystems.com</span>
    </li>
    <li class="contact">
      <svg class="contact__tag" viewBox="0 0 92 46"><path d="M0 0H68L92 23L68 46H0Z" fill="#000"/><use href="#icon-web" x="22" y="11" width="24" height="24" stroke="#e4e4e4"/></svg>
      <span class="contact__text">www.velmorisystems.com</span>
    </li>
  </ul>
  <p class="tagline">Custom Business Computers &amp; Consulting</p>
</section>

<!-- Black side -->
<section class="card card--gaming">
  <div class="photo" role="img" aria-label="Photo of a dark gaming PC setup with a glowing monitor and keyboard"></div>
  <div class="divider divider--top"></div>
  <div class="divider divider--bottom"></div>
  <div class="brand"><span class="brand__mark"></span>VELMORI</div>
  <div class="person">
    <p class="person__name">MARCO RUIZ DELAN</p>
    <p class="person__title">CEO &amp; Co-Founder</p>
  </div>
  <ul class="contacts">
    <li class="contact">
      <svg class="contact__tag" viewBox="0 0 92 46"><path d="M0 0H68L92 23L68 46H0Z" fill="#cbbfb2"/><use href="#icon-phone" x="22" y="11" width="24" height="24" fill="#000" stroke="#000"/></svg>
      <span class="contact__text">+52 5812 - 3390</span>
    </li>
    <li class="contact">
      <svg class="contact__tag" viewBox="0 0 92 46"><path d="M0 0H68L92 23L68 46H0Z" fill="#cbbfb2"/><use href="#icon-mobile" x="22" y="11" width="24" height="24" stroke="#000"/></svg>
      <span class="contact__text">+52 55 - 4168 - 0937</span>
    </li>
    <li class="contact">
      <svg class="contact__tag" viewBox="0 0 92 46"><path d="M0 0H68L92 23L68 46H0Z" fill="#cbbfb2"/><use href="#icon-mail" x="22" y="11" width="24" height="24" stroke="#000"/></svg>
      <span class="contact__text">contact@velmorisystems.com</span>
    </li>
    <li class="contact">
      <svg class="contact__tag" viewBox="0 0 92 46"><path d="M0 0H68L92 23L68 46H0Z" fill="#cbbfb2"/><use href="#icon-web" x="22" y="11" width="24" height="24" stroke="#000"/></svg>
      <span class="contact__text">www.velmorisystems.com</span>
    </li>
  </ul>
  <p class="tagline">Custom Gaming PC's</p>
</section>

</body>
</html>
```